Commercial Construction Company

We need a business card design based on our current logo. We are a commercial general contractor based in Southern California that specializes in bank remodels. We would like to see designs that incorporate dark blue. The final design should portray an image of professionalism and quality.

If possible, I would like to add metallic foil to the design. Thank you

```html
<!DOCTYPE html>
<html lang="en">
<head>
<meta charset="UTF-8">
<title>HCBG Business Card</title>
<link rel="stylesheet" href="https://fonts.googleapis.com/css2?family=Montserrat:wght@800&family=Open+Sans:wght@400;600&display=swap">
<style>
  :root {
    --stage: #2a2a2a;
    --brand-blue: #0e4a7f;
    --ink: #0a0a0a;
    --paper: #ffffff;
    --text: #1a1a1a;
    --rule: #2a5c99;
  }
  * { box-sizing: border-box; margin: 0; padding: 0; }
  html, body { width: 1200px; height: 900px; overflow: hidden; background: var(--stage); }
  .stage { position: relative; width: 1200px; height: 900px; }
  .card {
    position: absolute; left: 250px; width: 700px; height: 400px; overflow: hidden;
    box-shadow: 0 14px 30px rgba(0,0,0,.55);
  }
  .card-back { top: 35px; background: var(--brand-blue); }
  .card-front { top: 465px; background: var(--paper); }
  .back-band { position: absolute; inset: 0; }
  .back-mark {
    position: absolute; right: 70px; top: 150px;
    display: flex; align-items: center; gap: 14px;
  }
  .mark-dot { width: 22px; height: 22px; border-radius: 50%; background: var(--paper); }
  .back-mark .wordmark { color: var(--ink); }
  .wordmark {
    font-family: "Montserrat", sans-serif; font-weight: 800;
    font-size: 62px; letter-spacing: 1px; line-height: 1;
  }
  .front-mark {
    position: absolute; left: 48px; top: 52px;
    display: flex; align-items: center; gap: 14px;
  }
  .front-mark .mark-dot { background: var(--brand-blue); }
  .front-mark .wordmark { color: var(--ink); font-size: 56px; }
  .holder { position: absolute; left: 60px; top: 170px; }
  .holder-name {
    font-family: "Montserrat", sans-serif; font-weight: 800;
    font-size: 28px; color: var(--brand-blue); letter-spacing: .5px;
  }
  .holder-title { font-family: "Open Sans", sans-serif; font-size: 19px; color: var(--text); margin-top: 2px; }
  .divider { position: absolute; left: 60px; right: 60px; top: 258px; height: 1.5px; background: var(--rule); }
  .contacts {
    position: absolute; left: 60px; top: 278px; list-style: none;
    font-family: "Open Sans", sans-serif; font-size: 20px; color: var(--text);
  }
  .contacts li { display: flex; align-items: center; gap: 12px; line-height: 32px; }
  .contacts svg { width: 18px; height: 18px; flex: none; }
  .contacts .accent { color: var(--brand-blue); }
  .location {
    position: absolute; right: 60px; top: 310px;
    font-family: "Open Sans", sans-serif; font-size: 20px; color: var(--text);
  }
</style>
</head>
<body>
<main class="stage">
  <section class="card card-back" aria-label="Card back">
    <svg class="back-band" viewBox="0 0 700 400" preserveAspectRatio="none" aria-hidden="true">
      <path d="M0 0 L120 0 C160 200 380 350 700 340 L700 400 L0 400 Z" fill="var(--ink)"/>
      <path d="M0 0 L70 0 C120 230 330 390 560 400 L0 400 Z" fill="var(--ink)"/>
    </svg>
    <div class="back-mark">
      <span class="mark-dot"></span>
      <span class="wordmark">HCBG</span>
    </div>
  </section>

  <section class="card card-front" aria-label="Card front">
    <div class="front-mark">
      <span class="mark-dot"></span>
      <span class="wordmark">HCBG</span>
    </div>
    <div class="holder">
      <p class="holder-name">DANIEL MARSH</p>
      <p class="holder-title">Owner / CEO</p>
    </div>
    <div class="divider"></div>
    <ul class="contacts">
      <li>
        <svg viewBox="0 0 24 24" aria-hidden="true"><circle cx="12" cy="12" r="10" fill="none" stroke="var(--brand-blue)" stroke-width="1.8"/><path d="M8.5 7.5l2 2-1 1.5c.8 1.6 1.9 2.7 3.5 3.5l1.5-1 2 2-1.5 1.5c-3.5-.5-6.5-3.5-7-7z" fill="var(--brand-blue)"/></svg>
        <span>555 014 2290</span>
      </li>
      <li>
        <svg viewBox="0 0 24 24" aria-hidden="true"><rect x="2" y="5" width="20" height="14" fill="none" stroke="var(--brand-blue)" stroke-width="1.8"/><path d="M2 5l10 8 10-8" fill="none" stroke="var(--brand-blue)" stroke-width="1.8"/></svg>
        <span>info@hcbgbuild.com</span>
      </li>
      <li>
        <svg viewBox="0 0 24 24" aria-hidden="true"><circle cx="12" cy="12" r="10" fill="none" stroke="var(--brand-blue)" stroke-width="1.8"/><ellipse cx="12" cy="12" rx="4.5" ry="10" fill="none" stroke="var(--brand-blue)" stroke-width="1.5"/><path d="M2 12h20M4 7h16M4 17h16" stroke="var(--brand-blue)" stroke-width="1.3"/></svg>
        <span>www.<span class="accent">hcbgbuild</span>.com</span>
      </li>
    </ul>
    <p class="location">Southern California 92810</p>
  </section>
</main>
</body>
</html>
```